Business Card & Logo Design

Originally the brief was for a card only - I now think it's probably better to include a logo design as well. PLease add $200 to the Budget of $210, Apologies for the inconvenience for thaos that have already submitted designs.

Lantern Hollow Productions Pty Ltd is a video/dvd/ production company. Primarily corporate medium to high end. It's a one man operation that's been in business 20 years.

The name " Lantern Hollow" is a primarily a reference to Mathieu Corbelle film that's about film making. Shooting "Lantern Hollow" is also a technique employed by cinematographers to make scenes shot in daylight look like night.

See the design emphasising blue day/night tones but open to other ideas.

Main Text can either be Lantern Hollow Productions or Lantern Hollow.

Many thanks to all designers who submitted ideas for this brief.

Choosing between the designs was very difficult indeed.

I wish everyone the best and may the next job be yours!

Warren

• Text for card:
In Larger Print
Lantern Hollow Productions or Lantern Hollow
Warren Bellamy
In Smaller Print
Lantern Hollow Productions Pty Ltd.
17 Pelham Street
Ashcombe Vale, VIC, 3871
P: 9734 2061
m: 0438 725 190
e: warrenbellamy@ostrafel.com

```html
<!DOCTYPE html>
<html lang="en">
<head>
<meta charset="utf-8">
<title>Lantern Hollow Productions – Business Card</title>
<link rel="stylesheet" href="https://fonts.googleapis.com/css2?family=Old+Standard+TT:wght@400&display=swap">
<style>
  :root {
    --page: #ffffff;
    --card: #ffffff;
    --card-edge: #8c8c8c;
    --ink: #7a7a7a;
    --rule: #9a9a9a;
    --dawn: #ffd9bf;
    --dusk: #94a0ff;
    --shadow: rgba(0, 0, 0, 0.22);
  }
  * { box-sizing: border-box; margin: 0; padding: 0; }
  html, body {
    width: 1200px;
    height: 900px;
    overflow: hidden;
    background: var(--page);
  }
  body {
    position: relative;
    font-family: "Old Standard TT", "Century Schoolbook", Georgia, serif;
    color: var(--ink);
  }
  .card {
    position: absolute;
    width: 650px;
    height: 398px;
    border: 1px solid var(--card-edge);
    background: var(--card);
    box-shadow: 4px 5px 6px var(--shadow);
    overflow: hidden;
  }
  .card--front {
    left: 55px;
    top: 44px;
    background:
      linear-gradient(135deg, var(--dawn) 0%, rgba(255,255,255,0) 22%, rgba(255,255,255,0) 78%, var(--dusk) 100%),
      var(--card);
  }
  .card--back {
    left: 503px;
    top: 478px;
  }
  .wordmark {
    position: absolute;
    text-align: center;
  }
  .wordmark__name {
    display: block;
    font-variant: small-caps;
    white-space: nowrap;
    color: var(--ink);
    line-height: 1;
  }
  .wordmark__rule {
    display: block;
    height: 1px;
    background: var(--rule);
  }
  .wordmark__tag {
    display: block;
    text-transform: uppercase;
    color: var(--ink);
    line-height: 1;
  }
  .card--front .wordmark {
    left: 63px;
    top: 150px;
    width: 499px;
  }
  .card--front .wordmark__name {
    font-size: 58px;
    letter-spacing: 1px;
    padding-bottom: 10px;
  }
  .card--front .wordmark__tag {
    font-size: 16px;
    letter-spacing: 9px;
    margin-top: 12px;
  }
  .card--back .wordmark {
    left: 28px;
    top: 46px;
    width: 307px;
  }
  .card--back .wordmark__name {
    font-size: 36px;
    padding-bottom: 6px;
  }
  .card--back .wordmark__tag {
    font-size: 10.5px;
    letter-spacing: 5px;
    margin-top: 7px;
  }
  .contact {
    position: absolute;
    left: 33px;
    top: 196px;
    font-size: 15px;
    line-height: 19.5px;
    color: var(--ink);
  }
  .contact__address { margin-bottom: 19.5px; font-style: normal; }
  .contact__row { display: flex; }
  .contact__label { width: 22px; }
</style>
</head>
<body>

  <section class="card card--front" aria-label="Business card front">
    <div class="wordmark">
      <span class="wordmark__name">Lantern Hollow</span>
      <span class="wordmark__rule"></span>
      <span class="wordmark__tag">Productions</span>
    </div>
  </section>

  <section class="card card--back" aria-label="Business card back">
    <div class="wordmark">
      <span class="wordmark__name">Lantern Hollow</span>
      <span class="wordmark__rule"></span>
      <span class="wordmark__tag">Productions</span>
    </div>

    <div class="contact">
      <address class="contact__address">
        Warren Bellamy<br>
        Lantern Hollow Productions Pty Ltd.<br>
        17 Pelham Street<br>
        Ashcombe Vale, VIC, 3871
      </address>
      <div class="contact__row"><span class="contact__label">p</span><span>9734 2061</span></div>
      <div class="contact__row"><span class="contact__label">m</span><span>0438 725 190</span></div>
      <div class="contact__row"><span class="contact__label">e</span><span>warrenbellamy@ostrafel.com</span></div>
    </div>
  </section>

</body>
</html>
```